Tumbleroo Childcare centre needs a new LED outdoor banner

We need a new outdoor banner for our pre-school. It needs to be around 2440 mm x 1220 mm. It will be lit at night so I need it to stand out. I'm looking for a modern upbeat design. It will have my logo in the middle which is a graduation teddy bear with our name and phone number on it. I'm happy to experiment with different design options as mine is 20 years old. It needs to be colorful, inviting and very "in your face" and child friendly. It will be located near the fence of the property so it will be seen by cars driving by at a speed of around 50KM/H. So it needs to be clear, big bold fonts and bright colors. Thank you!

```html
<!DOCTYPE html>
<html lang="en">
<head>
<meta charset="utf-8">
<title>Tumbleroo Childcare Centre – Outdoor Banner</title>
<link rel="stylesheet" href="https://fonts.googleapis.com/css2?family=Fredoka:wght@600&display=swap">
<style>
  :root {
    --page: #e6e6e6;
    --sky-light: #ffffff;
    --sky-edge: #c9ecfb;
    --pink: #ec1b8c;
    --ink: #1a1a1a;
    --white: #ffffff;
    --yellow: #f5d316;
    --cyan: #38b8e6;
    --green: #3aa935;
    --orange: #f08a1c;
    --red: #e3202a;
    --purple: #8e2b8f;
    --magenta: #e0247a;
    --navy: #1f2375;
    --brown: #6b4522;
    --lime: #8cc63f;
  }
  * { margin: 0; padding: 0; box-sizing: border-box; }
  html, body {
    width: 1200px;
    height: 759px;
    overflow: hidden;
    background: var(--page);
  }
  .banner {
    position: absolute;
    left: 30px;
    top: 94px;
    width: 1140px;
    height: 570px;
    background: radial-gradient(ellipse at 50% 50%, var(--sky-light) 30%, var(--sky-edge) 100%);
    overflow: hidden;
    font-family: "Fredoka", "Arial Rounded MT Bold", sans-serif;
    font-weight: 600;
  }
  .crayon-column,
  .pencil-column {
    position: absolute;
    top: 0;
    width: 140px;
    height: 100%;
    background: linear-gradient(to bottom,
      var(--yellow) 0%, var(--cyan) 7%, var(--green) 14%, var(--orange) 21%,
      var(--red) 28%, var(--purple) 35%, var(--magenta) 42%, var(--navy) 49%,
      var(--brown) 56%, var(--lime) 63%, var(--yellow) 70%, var(--cyan) 77%,
      var(--green) 84%, var(--orange) 91%, var(--red) 100%);
  }
  .crayon-column { left: 0; }
  .pencil-column {
    right: 0;
    background: linear-gradient(to bottom,
      var(--orange) 0%, var(--cyan) 8%, var(--green) 15%, var(--orange) 22%,
      var(--red) 29%, var(--purple) 36%, var(--magenta) 43%, var(--navy) 50%,
      var(--brown) 57%, var(--lime) 64%, var(--orange) 71%, var(--cyan) 78%,
      var(--green) 85%, var(--orange) 92%, var(--red) 100%);
  }
  .centre-name {
    position: absolute;
    left: 140px;
    right: 140px;
    top: 110px;
    text-align: center;
    color: var(--pink);
    line-height: 1;
  }
  .centre-name .brand-line {
    display: block;
    font-size: 132px;
    letter-spacing: 1px;
  }
  .centre-name .tag-line {
    display: block;
    margin-top: 14px;
    font-size: 72px;
  }
  .phone-box {
    position: absolute;
    left: 260px;
    top: 434px;
    width: 620px;
    height: 92px;
    border: 3px solid var(--ink);
    border-radius: 46px;
    background: var(--white);
    display: flex;
    align-items: center;
    justify-content: center;
    color: var(--pink);
    font-size: 72px;
    letter-spacing: 4px;
  }
</style>
</head>
<body>
  <div class="banner">
    <div class="crayon-column" role="img" aria-label="Column of colourful wax crayons pointing right"></div>
    <div class="pencil-column" role="img" aria-label="Column of colourful pencils pointing left"></div>

    <h1 class="centre-name">
      <span class="brand-line">Tumbleroo</span>
      <span class="tag-line">Childcare Centre</span>
    </h1>

    <div class="phone-box">02 5550 1234</div>
  </div>
</body>
</html>
```